Business Card and Envelope Layout Change/Font Increase

Very simple job, sorry. I need the address on my envelope moved from the lower left corner and placed under my logo in the upper left corner and the overall font size of the address increased to about twice of what it is so it is easier to read. Also, on the envelope, my website and email address can remain in the lower right corner but I would like the font size also increased.
As for the business card, I would like the vertical "I speak Spanish/Yo hablo Espanol" removed. I would also like the font size of the text in the blue area slightly increased for easier reading. Final change are the credentials under the name. Please delete what is currently there (LMHC, NCC, DCC) and add the following: PhD., LMHC, CMHS, ACS.
I am attaching the eps files for the envelope and the photoshop file for the business card.
As described in the description, just some minor changes. I already have the files for the back of the business card as there are no changes for that.

```html
<!DOCTYPE html>
<html lang="en">
<head>
<meta charset="utf-8">
<title>Birchwell Counseling – Envelope</title>
<link rel="stylesheet" href="https://fonts.googleapis.com/css2?family=Hind:wght@400;500&family=Didact+Gothic&display=swap">
<style>
  :root {
    --brand-blue: #2c5f94;
    --brand-green: #437435;
    --text-blue: #2e5d99;
    --text-green: #437435;
    --paper: #ffffff;
  }
  * { margin: 0; padding: 0; box-sizing: border-box; }
  html, body {
    width: 1200px;
    height: 570px;
    overflow: hidden;
    background: var(--paper);
  }
  .envelope {
    position: relative;
    width: 1200px;
    height: 570px;
    background: var(--paper);
    overflow: hidden;
  }
  .envelope__bands {
    position: absolute;
    inset: 0;
    width: 1200px;
    height: 570px;
  }
  .band--blue { fill: var(--brand-blue); }
  .band--green { fill: var(--brand-green); }

  .brand {
    position: absolute;
    left: 80px;
    top: 132px;
    display: flex;
    align-items: center;
    gap: 14px;
  }
  .brand__dot {
    width: 34px;
    height: 34px;
    border-radius: 50%;
    background: var(--brand-green);
  }
  .brand__name {
    font-family: "Hind", sans-serif;
    font-weight: 500;
    font-size: 38px;
    line-height: 1;
    color: var(--text-blue);
    padding-top: 6px;
  }

  .return-address {
    position: absolute;
    left: 79px;
    top: 213px;
    font-family: "Hind", sans-serif;
    font-weight: 400;
    font-size: 21px;
    line-height: 29.5px;
    color: var(--text-blue);
    font-style: normal;
  }
  .return-address__phone { font-size: 19px; }

  .web-contact {
    position: absolute;
    right: 58px;
    top: 426px;
    text-align: right;
    font-family: "Didact Gothic", sans-serif;
    font-size: 18px;
    letter-spacing: 3.2px;
    line-height: 31px;
    color: var(--text-green);
  }
  .web-contact__line { display: block; }
</style>
</head>
<body>
  <main class="envelope">
    <svg class="envelope__bands" viewBox="0 0 1149 546" preserveAspectRatio="none" aria-hidden="true">
      <polygon class="band--blue" points="0,0 767,0 710,59 0,59"/>
      <polygon class="band--green" points="800,0 1149,0 1149,59 742,59"/>
      <polygon class="band--blue" points="0,486 723,486 697,546 0,546"/>
      <polygon class="band--green" points="757,486 1149,486 1149,546 700,546"/>
    </svg>

    <div class="brand">
      <span class="brand__dot" aria-hidden="true"></span>
      <span class="brand__name">Birchwell Counseling</span>
    </div>

    <address class="return-address">
      4180 Harborview Ave, Suite B2<br>
      Fairmont, WA 98312<br>
      <span class="return-address__phone">Tel: 360 / 555 - 0148</span>
    </address>

    <div class="web-contact">
      <span class="web-contact__line">hello@birchwellcounseling.com</span>
      <span class="web-contact__line">www.birchwellcounseling.com</span>
    </div>
  </main>
</body>
</html>
```